User Interface Designer Needed

I need a few designs for a property law comparison website. We assist the public with finding a solicitor for the purchase or sale of their house and units. We are currently in the process of creating a questionnaire based woo commerce product filter using gravity forms. I'd like to see designs that use the logo colours. Users will be selecting options such as "Buying" or "Selling", they will then be selecting options such as "House" "Unit" or "Land". Details attached. The final design should communicate ease and simplicity. Questions will be answered one at a time, and the next question is dependent on the answer to the question prior

Target Market(s)

First home buyers, people from ages 18-80 make and female looking to get rid of the hassle of ringing around and going from website to website trying to get a quote

Industry/Entity Type

Real Estate

Number of Pages Required

1 page

Colors
33a6d7

Requirements
Must have
• A design for every question
Nice to have
• Simple symbols or simplistic pictures incorporated, even better if you can turn the question into a picture instead of words eg. A picture of a house, a picture of a unit and a picture of land instead of written answers

```html
<!DOCTYPE html>
<html lang="en">
<head>
<meta charset="utf-8">
<title>Get your quotes – Homvera</title>
<link href="https://fonts.googleapis.com/css2?family=Open+Sans:wght@300;400;700&family=Roboto+Condensed:wght@700&display=swap" rel="stylesheet">
<style>
  :root {
    --brand: #06a6d9;
    --brand-light: #9adcf3;
    --ink: #4a4a4a;
    --ink-soft: #555;
    --muted: #c8c8c8;
    --rule: #dcdcdc;
    --band: #524f50;
    --white: #ffffff;
  }
  * { box-sizing: border-box; margin: 0; padding: 0; }
  html, body { width: 1200px; height: 1200px; overflow: hidden; background: var(--white); }
  body { position: relative; font-family: "Open Sans", sans-serif; color: var(--ink); }

  .site-header { position: absolute; top: 0; left: 0; width: 1200px; height: 120px; }
  .brand { position: absolute; left: 144px; top: 46px; display: flex; align-items: center; gap: 8px; }
  .brand-dot { width: 34px; height: 34px; border-radius: 50%; background: var(--brand); }
  .brand-name { font-weight: 700; font-size: 30px; color: var(--brand); letter-spacing: -0.5px; }
  .main-nav { position: absolute; top: 59px; left: 0; width: 1200px; }
  .main-nav a { position: absolute; font-size: 11px; color: #444; text-decoration: none; white-space: nowrap; }
  .cart-icon { position: absolute; left: 1045px; top: 61px; }

  .intro { position: absolute; top: 172px; left: 0; width: 1200px; text-align: center; }
  .intro h1 { font-size: 37px; font-weight: 700; color: var(--ink); }
  .intro p { margin: 22px auto 0; width: 720px; font-size: 14.5px; font-weight: 300; line-height: 20px; color: #444; }

  .steps { position: absolute; top: 349px; left: 349px; width: 489px; height: 25px; border-bottom: 1px solid var(--rule); }
  .step { position: absolute; top: 0; font-size: 14px; color: var(--muted); white-space: nowrap; }
  .step.is-active { color: #333; }

  .area { position: absolute; top: 456px; left: 0; width: 1200px; height: 48px; }
  .area-label { position: absolute; left: 415px; top: 8px; font-size: 21px; font-weight: 300; color: #444; }
  .area-value { position: absolute; left: 483px; top: 7px; font-size: 21px; font-weight: 700; color: var(--ink); }
  .area-map { position: absolute; left: 595px; top: 0; width: 95px; height: 47px; border-radius: 10px 14px 18px 8px;
    background: linear-gradient(90deg, var(--brand) 0 38%, var(--brand-light) 38% 100%); }
  .area-change { position: absolute; left: 719px; top: 11px; font-size: 15px; color: var(--brand); text-decoration: underline; }

  .question { position: absolute; top: 552px; left: 0; width: 1200px; text-align: center; font-size: 35px; font-weight: 300; color: #444; }

  .choice { position: absolute; top: 656px; width: 134px; height: 134px; border: 2.5px solid var(--brand); border-radius: 5px; background: var(--white); }
  .choice.is-selected { background: var(--brand); }
  .choice-figure { position: absolute; left: 50%; top: 22px; transform: translateX(-50%); height: 78px; border-radius: 22px 22px 4px 4px; background: var(--brand); }
  .choice.is-selected .choice-figure { background: var(--white); }
  .choice-label { position: absolute; left: 0; right: 0; top: 104px; text-align: center; font-family: "Roboto Condensed", sans-serif; font-weight: 700; font-size: 16px; color: var(--brand); }
  .choice.is-selected .choice-label { color: var(--white); }

  .next-button { position: absolute; left: 497px; top: 861px; width: 210px; height: 52px; background: var(--brand); color: var(--white); font-size: 22px; font-weight: 300; text-align: center; line-height: 52px; }

  .testimonials { position: absolute; top: 1026px; left: 0; width: 1200px; height: 174px; background: var(--band); text-align: center; color: var(--white); }
  .testimonials h2 { margin-top: 41px; font-size: 38px; font-weight: 700; }
  .testimonials p { margin-top: 4px; font-size: 17px; }
</style>
</head>
<body>
  <header class="site-header">
    <div class="brand"><span class="brand-dot"></span><span class="brand-name">Homvera.com.au</span></div>
    <nav class="main-nav">
      <a style="left:609px">HOME</a>
      <a style="left:663px">FIXED FEES</a>
      <a style="left:740px">ARTICLES</a>
      <a style="left:807px">COMPANY</a>
      <a style="left:884px">CONTACT</a>
      <a style="left:961px">SIGN UP!</a>
    </nav>
    <svg class="cart-icon" width="11" height="10" viewBox="0 0 11 10" aria-label="Cart">
      <path d="M0 0.5h2l1.5 6h6l1.2-4.5H3" fill="none" stroke="#222" stroke-width="1.4"/>
      <rect x="3" y="2" width="7.5" height="4" fill="#222"/>
      <circle cx="4" cy="8.8" r="1" fill="#222"/><circle cx="9" cy="8.8" r="1" fill="#222"/>
    </svg>
  </header>

  <section class="intro">
    <h1>Get your quotes</h1>
    <p>This questionnaire will help you get quotes from property lawyers.&nbsp; Define your status, your property type and other significant contract details that will help you avoid unexpected fees</p>
  </section>

  <div class="steps">
    <span class="step is-active" style="left:9px">1. YOUR STATUS</span>
    <span class="step" style="left:173px">2. PROPERTY TYPE</span>
    <span class="step" style="left:345px">3. QUOTE EXTRAS</span>
  </div>

  <div class="area">
    <span class="area-label">Area:</span>
    <span class="area-value">Western</span>
    <div class="area-map" role="img" aria-label="Map of the country with the western region highlighted"></div>
    <a class="area-change">Change</a>
  </div>

  <div class="question">I am a...</div>

  <div class="choice" style="left:378px">
    <div class="choice-figure" style="width:60px" role="img" aria-label="Buyer figure"></div>
    <div class="choice-label">BUYER</div>
  </div>
  <div class="choice is-selected" style="left:537px">
    <div class="choice-figure" style="width:60px" role="img" aria-label="Seller figure"></div>
    <div class="choice-label">SELLER</div>
  </div>
  <div class="choice" style="left:696px">
    <div class="choice-figure" style="width:106px; top:30px; height:70px" role="img" aria-label="Buyer and seller figures"></div>
    <div class="choice-label">BUYER &amp; SELLER</div>
  </div>

  <div class="next-button">NEXT</div>

  <section class="testimonials">
    <h2>Our Customers Love Us</h2>
    <p>Don’t Just Take Our Word For It, Read It From Them</p>
  </section>
</body>
</html>
```